Trade Show Flier for CleanTech Battery Company
Halden Vore Partners
Company Overview, Corporate Partners, Product Specifications
Halden Vore Partners is a cleantech startup developing large commercial size redox flow batteries. These batteries are used for providing backup power to buildings and for helping to integrate solar and wind energy into the electricity grid.
Energy
Corporate - will distribute fliers at trade show to potential partners, investors, researchers, etc.
Want a clean & modern look. See www.haldenvorepartners.example for corporate colors and design theme. Template will be used for a variety of materials such as specifications sheet, corporate overview, etc.
HVP Corporate Logo
HVP Corporate Name and Logo

```html
<!DOCTYPE html>
<html lang="en">
<head>
<meta charset="utf-8">
<title>Halden Vore Partners – Trade Show Flier</title>
<link rel="stylesheet" href="https://fonts.googleapis.com/css2?family=Open+Sans:ital,wght@0,400;0,600;0,700;1,700&display=swap">
<style>
:root{
  --backdrop:#4a3a30;
  --navy:#0f2f6b;
  --blue:#1c4f9c;
  --sky:#3f7fc8;
  --pale:#e8eef7;
  --row:#f1f4f9;
  --rule:#c9d4e4;
  --ink:#3a3f47;
  --green:#4da64a;
  --white:#ffffff;
  --photo-cool:#9fb9d8;
  --photo-warm:#b98a72;
}
*{box-sizing:border-box;margin:0;padding:0}
html,body{width:1200px;height:790px;overflow:hidden}
body{background:var(--backdrop);font-family:"Open Sans",Arial,sans-serif;color:var(--ink);position:relative}
.page{position:absolute;top:6px;height:778px;background:var(--white);overflow:hidden;box-shadow:0 2px 8px rgba(0,0,0,.4)}
.page--overview{left:19px;width:568px}
.page--specs{left:606px;width:578px}
.abs{position:absolute}
.body-text{font-size:9.5px;line-height:13.5px}
.body-text p+p{margin-top:8px}

/* overview header */
.hero{left:0;top:0;width:568px;height:232px;background:linear-gradient(180deg,#f4f8fd 0%,#dfe9f6 100%)}
.brand{left:16px;top:16px;display:flex;align-items:center;gap:10px}
.brand__dot{width:40px;height:40px;border-radius:50%;background:var(--blue)}
.brand__name{font-size:38px;font-weight:700;color:var(--blue);letter-spacing:2px;line-height:1}
.brand__sub{left:68px;top:58px;font-size:8px;font-weight:600;color:var(--blue);letter-spacing:1.5px}
.tagline{left:0;top:92px;width:340px;height:72px;padding:10px 16px;background:linear-gradient(90deg,var(--blue),rgba(28,79,156,0));color:var(--white);font-size:21px;font-weight:700;font-style:italic;line-height:26px}
.thumb{top:172px;width:112px;height:52px;border:2px solid var(--white)}
.thumb--bridge{left:16px;background:var(--photo-cool)}
.thumb--desert{left:134px;background:var(--photo-warm)}
.hero-photo{left:360px;top:18px;width:196px;height:206px;border-radius:6px;background:linear-gradient(180deg,#cfe0f2,#8fb6dc)}

.section-head{display:flex;align-items:center;gap:8px;font-weight:700;color:var(--blue)}
.section-head__icon{width:20px;height:20px;border-radius:50%;background:var(--blue);flex:none}
.section-head--lg{font-size:16px}
.section-head--md{font-size:13px}

.features{left:374px;top:232px;width:186px;height:236px;background:linear-gradient(180deg,var(--navy),var(--blue));padding:12px 12px;color:var(--white)}
.features li{list-style:none;font-size:8.6px;line-height:11.5px;padding-left:11px;position:relative;margin-bottom:6px}
.features li::before{content:"";position:absolute;left:0;top:4px;width:5px;height:5px;background:var(--white)}

.data-table{border-collapse:collapse;width:100%;font-size:8.5px}
.data-table th{background:var(--navy);color:var(--white);font-weight:600;text-align:left;padding:4px 6px}
.data-table td{padding:4px 6px;border-bottom:1px solid var(--rule)}
.data-table tr:nth-child(even) td{background:var(--row)}
.data-table .num{text-align:right}

.footer{left:0;top:730px;width:568px;height:48px;border-top:3px solid var(--blue);background:var(--pale);display:flex;align-items:center;justify-content:space-between;padding:0 16px;font-size:9px}
.social{display:flex;gap:6px}
.social span{width:18px;height:18px;background:var(--sky);border-radius:3px}

/* specs page */
.banner{left:0;top:0;width:578px;height:112px;background:var(--navy);color:var(--white);font-size:12.5px;font-weight:700;line-height:17px;text-align:center;padding:18px 34px}
.landscape{left:0;top:112px;width:578px;height:200px;background:linear-gradient(180deg,var(--photo-cool),var(--photo-warm))}
.spec-table{border-collapse:collapse;width:100%;font-size:9px}
.spec-table td{padding:9px 8px;border:1px solid var(--rule)}
.spec-table td:first-child{color:var(--ink);width:62%;font-size:8.5px;line-height:11px;padding:5px 8px}
.spec-table td:last-child{text-align:center;font-weight:600}
.spec-table tr:nth-child(odd) td{background:var(--row)}
.callout{left:365px;top:572px;width:200px;height:132px;background:var(--blue);color:var(--white);font-size:10px;font-weight:600;line-height:13.5px;text-align:center;padding:12px 12px}
.product-table th{text-align:center}
</style>
</head>
<body>

<section class="page page--overview">
  <header class="abs hero">
    <div class="abs brand"><span class="brand__dot"></span><span class="brand__name">HVP</span></div>
    <div class="abs brand__sub">HALDEN VORE PARTNERS</div>
    <div class="abs tagline">Any tagline or any other words can go here</div>
    <div class="abs thumb thumb--bridge" role="img" aria-label="Photo of a bridge over water"></div>
    <div class="abs thumb thumb--desert" role="img" aria-label="Photo of a desert landscape"></div>
    <div class="abs hero-photo" role="img" aria-label="Photo of two hands holding a glass globe with a tree inside"></div>
  </header>

  <h2 class="abs section-head section-head--lg" style="left:16px;top:244px"><span class="section-head__icon"></span>Halden Vore Partners Inc.</h2>
  <div class="abs body-text" style="left:16px;top:276px;width:346px">
    <p>Halden Vore Partners Inc. (HVP) began as a garage project in 2011 aiming to develop a cost effective energy storage solution to better align the supply and demand of electricity. HVP's initial innovations focused on improving the performance of conventional flow battery designs, eventually resulting in a low cost power density improvement over commercial batteries with similar chemistries on the market at the time. Recently, HVP has taken advantage of its high performance battery design to apply its efforts to the development of new redox chemistries whose electrolytes are composed of inexpensive earth abundant materials.</p>
    <p>Lorem ipsum dolor sit amet, consectetur adipiscing elit, sed do eiusmod tempor incididunt ut labore et dolore magna aliqua. Ut enim ad minim veniam, quis nostrud exercitation ullamco laboris nisi ut aliquip ex ea commodo consequat.</p>
  </div>
  <ul class="abs features">
    <li>Lorem ipsum dolor sit amet, consectetur adipiscing elit, sed do</li>
    <li>Eiusmod tempor incididunt ut labore et dolore magna aliqua. Ut</li>
    <li>Enim ad minim veniam, quis nostrud exercitation ullamco laboris nisi ut</li>
    <li>Aliquip ex ea commodo consequat</li>
    <li>Duis aute irure dolor in reprehenderit</li>
    <li>Velit in voluptate esse cillum dolore eu fugiat nulla pariatur</li>
    <li>Excepteur sint occaecat cupidatat non proident, sunt in culpa qui</li>
    <li>Officia deserunt mollit anim id est laborum</li>
  </ul>

  <h3 class="abs section-head section-head--md" style="left:16px;top:490px"><span class="section-head__icon"></span>Lorem Ipsum Dolor Set Emet</h3>
  <div class="abs" style="left:16px;top:520px;width:262px">
    <table class="data-table">
      <tr><th>Lorem ipsum dolor sit amet</th><th class="num">Monthly Price</th></tr>
      <tr><td>Lorem ipsum dolor sit amet</td><td class="num">$00.00</td></tr>
      <tr><td>Consectetur adipiscing elit</td><td class="num">$00.00</td></tr>
      <tr><td>Sed do eiusmod tempor</td><td class="num">$00.00</td></tr>
      <tr><th>Lorem ipsum dolor sit amet</th><th class="num">Monthly Price</th></tr>
      <tr><td>Incididunt ut labore et dolore</td><td class="num">$00.00</td></tr>
      <tr><td>Magna aliqua ut enim</td><td class="num">$00.00</td></tr>
      <tr><td>Ad minim veniam quis</td><td class="num">$00.00</td></tr>
      <tr><td>Nostrud exercitation ullamco</td><td class="num">$00.00</td></tr>
    </table>
  </div>

  <h3 class="abs section-head section-head--md" style="left:296px;top:490px"><span class="section-head__icon"></span>Cost Comparison Chart</h3>
  <svg class="abs" style="left:296px;top:520px" width="264" height="190" viewBox="0 0 264 190" aria-label="Bar chart comparing costs">
    <g stroke="#d5dbe5" stroke-width="1">
      <line x1="26" y1="20" x2="260" y2="20"/><line x1="26" y1="50" x2="260" y2="50"/>
      <line x1="26" y1="80" x2="260" y2="80"/><line x1="26" y1="110" x2="260" y2="110"/>
      <line x1="26" y1="140" x2="260" y2="140"/>
    </g>
    <line x1="26" y1="10" x2="26" y2="160" stroke="#8a94a3"/>
    <line x1="26" y1="160" x2="260" y2="160" stroke="#8a94a3"/>
    <g font-size="7" fill="#6a7380" text-anchor="end">
      <text x="22" y="23">50</text><text x="22" y="53">40</text><text x="22" y="83">30</text>
      <text x="22" y="113">20</text><text x="22" y="143">10</text><text x="22" y="163">0</text>
    </g>
    <g fill="#1c4f9c">
      <rect x="36" y="104" width="10" height="56"/><rect x="82" y="92" width="10" height="68"/>
      <rect x="128" y="80" width="10" height="80"/><rect x="174" y="68" width="10" height="92"/>
      <rect x="220" y="56" width="10" height="104"/>
    </g>
    <g fill="#4da64a">
      <rect x="47" y="120" width="10" height="40"/><rect x="93" y="110" width="10" height="50"/>
      <rect x="139" y="96" width="10" height="64"/><rect x="185" y="86" width="10" height="74"/>
      <rect x="231" y="74" width="10" height="86"/>
    </g>
    <g fill="#3f7fc8">
      <rect x="58" y="130" width="10" height="30"/><rect x="104" y="124" width="10" height="36"/>
      <rect x="150" y="114" width="10" height="46"/><rect x="196" y="104" width="10" height="56"/>
      <rect x="242" y="94" width="10" height="66"/>
    </g>
    <polyline points="46,96 92,84 138,66 184,52 230,36" fill="none" stroke="#0f2f6b" stroke-width="1.5"/>
    <g font-size="7" fill="#6a7380" text-anchor="middle">
      <text x="52" y="172">2008</text><text x="98" y="172">2009</text><text x="144" y="172">2010</text>
      <text x="190" y="172">2011</text><text x="236" y="172">2012</text>
    </g>
    <g font-size="7" fill="#3a3f47">
      <rect x="60" y="180" width="7" height="7" fill="#1c4f9c"/><text x="70" y="186">Series 1</text>
      <rect x="112" y="180" width="7" height="7" fill="#4da64a"/><text x="122" y="186">Series 2</text>
      <rect x="164" y="180" width="7" height="7" fill="#3f7fc8"/><text x="174" y="186">Series 3</text>
    </g>
  </svg>

  <footer class="abs footer">
    <span>© 2009-2012 Halden Vore Partners</span>
    <span class="social"><span></span><span></span><span></span></span>
  </footer>
</section>

<section class="page page--specs">
  <div class="abs banner">Lorem ipsum dolor sit amet, consectetur adipiscing elit, sed do eiusmod tempor incididunt ut labore et dolore magna aliqua. Ut enim ad minim veniam, quis nostrud exercitation ullamco laboris nisi ut aliquip ex ea commodo consequat.</div>
  <div class="abs landscape" role="img" aria-label="Photo of red rock cliffs under a blue sky"></div>

  <h2 class="abs section-head section-head--md" style="left:15px;top:326px"><span class="section-head__icon"></span>Lorem Ipsum Dolor Set Emet</h2>
  <div class="abs body-text" style="left:15px;top:356px;width:338px">
    <p>Halden Vore Partners Inc. (HVP) began as a garage project in 2011 aiming to develop a cost effective energy storage solution to better align the supply and demand of electricity. HVP's initial innovations focused on improving the performance of conventional flow battery designs, resulting in a low cost power density improvement over commercial batteries with similar chemistries on the market at the time.</p>
    <p>Lorem ipsum dolor sit amet, consectetur adipiscing elit, sed do eiusmod tempor incididunt ut labore et dolore magna aliqua. Ut enim ad minim veniam, quis nostrud exercitation ullamco laboris nisi ut aliquip ex ea commodo consequat.</p>
  </div>
  <div class="abs" style="left:15px;top:530px;width:338px">
    <table class="data-table product-table">
      <tr><th></th><th>Product</th><th>Product</th><th>Product</th></tr>
      <tr><td>Lorem ipsum dolor</td><td></td><td></td><td></td></tr>
      <tr><td>Sit amet consectetur</td><td></td><td></td><td></td></tr>
      <tr><td>Adipiscing elit sed</td><td></td><td></td><td></td></tr>
      <tr><td>Do eiusmod tempor</td><td></td><td></td><td></td></tr>
      <tr><td>Incididunt ut labore</td><td></td><td></td><td></td></tr>
      <tr><td>Et dolore magna</td><td></td><td></td><td></td></tr>
    </table>
  </div>
  <div class="abs body-text" style="left:15px;top:700px;width:338px">
    <p>Lorem ipsum dolor sit amet, consectetur adipiscing elit, sed do eiusmod tempor incididunt ut labore et dolore magna aliqua. Ut enim ad minim veniam, quis nostrud exercitation ullamco laboris nisi ut aliquip ex ea commodo consequat.</p>
  </div>

  <div class="abs" style="left:365px;top:324px;width:200px">
    <table class="spec-table">
      <tr><td>Lorem ipsum dolor sit amet</td><td>10%</td></tr>
      <tr><td>Lorem ipsum dolor sit amet</td><td>20%</td></tr>
      <tr><td>Lorem ipsum dolor sit amet</td><td>30%</td></tr>
      <tr><td>Lorem ipsum dolor sit amet</td><td>40%</td></tr>
      <tr><td>Lorem ipsum dolor sit amet</td><td>50%</td></tr>
      <tr><td>Lorem ipsum dolor sit amet</td><td>60%</td></tr>
    </table>
  </div>
  <div class="abs callout">Lorem ipsum dolor sit amet, consectetur adipiscing elit, sed do eiusmod tempor incididunt ut labore et dolore magna aliqua. Ut enim ad minim veniam, quis nostrud exercitation ullamco laboris nisi ut aliquip ex ea commodo consequat.</div>
  <div class="abs body-text" style="left:365px;top:712px;width:200px">
    <p>Lorem ipsum dolor sit amet, consectetur adipiscing elit, sed do eiusmod tempor incididunt ut labore et dolore magna aliqua. Ut enim ad minim veniam, quis nostrud exercitation.</p>
  </div>
</section>

</body>
</html>
```